Tovani Nightclub

Nightclub flyer., digital single sided, for FB and IG. I included samples of some previous flyers we've used. Sample Info:
TOVANI
FRIDAYS
FRI MAY 1 2020
DJ BRAVURA (club floor)
DJ ZOLT & DJ RAF (residents on the lounge floor)
4372 Birch Street Sacramento
www.tovanimurcott.com for list/VIP inquiries

Target Market(s)

Upscale top 40 crowd but want some cool and artsy like the examples included.

Font styles to use
Sans Serif

Requirements
Must have
• Tovani Logo
Nice to have
• Would be nice if the flyer can be incorporated later with DJ photos (sometimes we will add dj photos to instagram etc). Would like a big city type of feel.
Should not have
• Nothing too sexual.

```html
<!DOCTYPE html>
<html lang="en">
<head>
<meta charset="utf-8">
<title>Tovani Nightclub – Friday</title>
<link rel="stylesheet" href="https://fonts.googleapis.com/css2?family=Roboto:wght@300;400;700&display=swap">
<style>
  :root {
    --deep-violet: #2a0a4a;
    --violet: #7a10c8;
    --magenta: #e0169c;
    --hot-pink: #ff2fa8;
    --night: #14041f;
    --white: #ffffff;
    --logo-gold: #d9b85a;
    --logo-ink: #3a2a40;
  }
  * { margin: 0; padding: 0; box-sizing: border-box; }
  html, body {
    width: 959px; height: 1200px; overflow: hidden;
    background: var(--night);
  }
  .flyer {
    position: relative;
    width: 959px; height: 1200px;
    overflow: hidden;
    font-family: "Roboto", Arial, sans-serif;
    color: var(--white);
  }
  .stage-photo {
    position: absolute; inset: 0;
    background:
      radial-gradient(ellipse 260px 320px at 400px 520px, var(--hot-pink) 0%, rgba(224,22,156,0.6) 40%, rgba(224,22,156,0) 100%),
      radial-gradient(ellipse 120px 360px at 40px 620px, rgba(210,170,255,0.55), rgba(210,170,255,0) 100%),
      radial-gradient(ellipse 120px 360px at 570px 640px, rgba(220,190,255,0.5), rgba(220,190,255,0) 100%),
      radial-gradient(ellipse 120px 360px at 900px 640px, rgba(220,190,255,0.45), rgba(220,190,255,0) 100%),
      linear-gradient(180deg, #2b0838 0%, #5a0f80 30%, var(--violet) 55%, #4a0b86 75%, var(--night) 100%);
  }
  .stage-photo::after {
    content: ""; position: absolute; inset: 0;
    background: linear-gradient(90deg, rgba(20,4,31,0.75) 0%, rgba(20,4,31,0.35) 25%, rgba(20,4,31,0) 45%, rgba(20,4,31,0) 100%),
                linear-gradient(180deg, rgba(0,0,0,0) 70%, rgba(20,4,31,0.7) 100%);
  }
  .brand {
    position: absolute; left: 0; right: 0; top: 86px;
    text-align: center;
  }
  .brand-dot {
    display: block; width: 32px; height: 32px; margin: 0 auto 8px;
    border-radius: 50%; background: var(--logo-gold);
  }
  .brand-name {
    font-size: 16px; font-weight: 400; letter-spacing: 0.04em;
    color: var(--logo-ink);
  }
  .text { position: absolute; white-space: nowrap; line-height: 1; }
  .headline {
    left: 0; right: 0; top: 216px; text-align: center;
    font-size: 166px; font-weight: 400; letter-spacing: 0.19em;
    padding-left: 0.19em;
  }
  .event-date {
    left: 0; right: 0; top: 373px; text-align: center;
    font-size: 43px; font-weight: 400; letter-spacing: 0.02em;
  }
  .venue-address {
    left: 0; right: 0; top: 847px; text-align: center;
    font-size: 22px; font-weight: 700; letter-spacing: 0.03em;
  }
  .venue-site {
    left: 0; right: 0; top: 899px; text-align: center;
    font-size: 21px; font-weight: 400; letter-spacing: 0.05em;
  }
  .club-floor { left: 40px; top: 1006px; width: 400px; text-align: center; }
  .lounge-floor { left: 500px; top: 974px; width: 440px; text-align: center; }
  .dj-name { display: block; font-size: 56px; font-weight: 400; letter-spacing: 0.02em; line-height: 1; }
  .amp { font-size: 28px; margin-right: 6px; }
  .floor-note { display: block; font-size: 24px; font-weight: 400; letter-spacing: 0.03em; margin-top: 4px; }
  .lounge-floor .dj-name + .dj-name { margin-top: 8px; }
</style>
</head>
<body>
  <main class="flyer">
    <div class="stage-photo" role="img" aria-label="Photo of a DJ in silhouette at the decks, lit by magenta and violet stage lights"></div>

    <div class="brand">
      <span class="brand-dot"></span>
      <div class="brand-name">TOVANI</div>
    </div>

    <h1 class="text headline">FRIDAY</h1>
    <p class="text event-date">FRI MAY 1 2020</p>

    <p class="text venue-address">4372 Birch Street Sacramento</p>
    <p class="text venue-site">www.tovanimurcott.com for list/VIP inquiries</p>

    <section class="text club-floor">
      <span class="dj-name">DJ BRAVURA</span>
      <span class="floor-note">(Club Floor)</span>
    </section>

    <section class="text lounge-floor">
      <span class="dj-name">DJ ZOLT</span>
      <span class="dj-name"><span class="amp">&amp;</span>DJ RAF</span>
      <span class="floor-note">(Residents on The Lounge Floor)</span>
    </section>
  </main>
</body>
</html>
```